Lantern and Keystone Website

We are a private investigation that people turn to when they seek answers. We provide all types of investigation services as well as security and debt collection but mainly we specialise in digital forensic investigation. This site will be the first representation that potential clients see. We need a site that can work on all browsers so not too many animations. The theme we are going for is "Hollow" the TV show but keeping the law enforcement look. We want it to expand on the logo of our company that is strength and pride (refer to files attached). The logo and mission statement must stand out.
The relevant info is attached in .doc documents

Hi,

I have uploaded a slightly different version of the logo and I do prefer the new version and made a FEW but important updates and additions to the website info. Sorry for the inconvenience.

Hi, 

Sorry just one last thing can you please put the following on the website 'Lantern and Keystone is a South Australian owned business and we service all of Australia.' 

I have increased the budget.

Hi,

I've increased the budget slightly. I will continue to increase it as long as the quality of designs match it.

I have increased the budget. I will increase it more if I see some designs that warrant the increase.

I have extended the deadline by 3 days.

Hi,

Forget the brief and please take a look at this link and that is the type of design I want. I want people to look at it and think modern, professional, digital, forensic investigation. I have not seen anything that makes me think "wow" so please submit some new designs. I will increase the budget when I start to see designs that I like. 

regarding the last message, this is the link

https://www.brelvanoffice.example

Reason: Have not seen anything that stands out from the rest.

Reason: To let designers finish off their current concepts that they may be working on.

Target Market(s)

Average to corporate people seeking professionalism and a firm that can supply answers that traditional law enforcement agencies fail to provide

Industry/Entity Type

Security

Requirements
Must have
• A professional NRB, Coastal Ward Constabulary website look mixed with a theme from the TV show "Hollow" and the ability to download the business cards (refer to attached files)
Should not have
• cartoon images and anything relating to Percival Thorne

```html
<!DOCTYPE html>
<html lang="en">
<head>
<meta charset="utf-8">
<title>Lantern and Keystone</title>
<link href="https://fonts.googleapis.com/css2?family=PT+Sans:wght@400;700&family=Open+Sans:wght@300;400&display=swap" rel="stylesheet">
<style>
  :root{
    --paper:#e3e3e2;
    --paper-dark:#d6d6d5;
    --ink:#3a3a3a;
    --nav-active:#2e2e2e;
    --night:#0b0b0c;
    --band:#1d1b18;
    --band-line:#2c2a26;
    --band-head:#8d8d8d;
    --band-text:#757370;
    --statement:#4a4843;
    --gold:#c6b97f;
    --gold-deep:#a8841e;
    --muted:#8c8c8c;
    --heading-grey:#9a9a9a;
    --rule:#cfcfcf;
    --accent-red:#c0392b;
    --footer:#9b9b9b;
  }
  *{margin:0;padding:0;box-sizing:border-box}
  html,body{width:1105px;height:1200px;overflow:hidden}
  body{position:relative;background:var(--paper);font-family:"Open Sans",Arial,sans-serif;color:var(--ink)}
  .abs{position:absolute}

  /* header */
  .site-header{position:absolute;left:0;top:0;width:1105px;height:112px;background:radial-gradient(circle at 30% 40%,#ececeb,var(--paper) 60%,var(--paper-dark));border-bottom:2px solid #f4f4f4}
  .brand{position:absolute;left:128px;top:52px;display:flex;align-items:center;gap:10px}
  .brand-mark{width:34px;height:34px;border-radius:50%;background:var(--gold-deep)}
  .brand-name{font-family:"PT Sans",sans-serif;font-weight:700;font-size:17px;color:var(--ink);line-height:1.15;width:110px}
  .utility{position:absolute;left:900px;top:20px;font-family:"PT Sans",sans-serif;font-size:11px;color:#8a8a8a;letter-spacing:.5px}
  .header-rule{position:absolute;left:292px;top:50px;width:708px;height:1px;background:#cacaca}
  .main-nav{position:absolute;left:412px;top:65px;display:flex;font-family:"PT Sans",sans-serif;font-size:15.5px;color:#3a3a3a}
  .main-nav a{color:inherit;text-decoration:none;height:32px;line-height:32px;padding:0 14px;margin-right:28px}
  .main-nav a.is-active{background:var(--nav-active);color:#fff;border-radius:2px;border:1px solid #111}

  /* hero */
  .hero{position:absolute;left:0;top:112px;width:1105px;height:407px;background:linear-gradient(90deg,var(--night) 0%,#121417 45%,#1c2532 100%)}
  .hero-photo{position:absolute;right:0;top:0;width:600px;height:407px;background:radial-gradient(ellipse at 70% 30%,#4a5d85 0%,#26314a 45%,rgba(12,13,16,0) 80%)}
  .hero-title{position:absolute;left:107px;top:140px;width:380px;font-weight:300;font-size:24px;line-height:28px;color:#c9c9c9}
  .btn-gold{position:absolute;left:107px;top:244px;width:77px;height:33px;background:var(--gold);color:#3a3a30;font-size:14px;line-height:33px;text-align:center;border-radius:2px}

  /* services band */
  .band{position:absolute;left:0;top:519px;width:1105px;height:294px;background:linear-gradient(180deg,#1a1916,var(--band) 40%,#15130f)}
  .statement{position:absolute;left:128px;top:16px;width:860px;font-weight:300;font-size:18.5px;line-height:27.5px;color:var(--statement);text-transform:uppercase;letter-spacing:-.3px}
  .band-rule{position:absolute;left:0;top:111px;width:1105px;height:1px;background:var(--band-line)}
  .feature{position:absolute;top:125px}
  .feature h3{font-family:"PT Sans",sans-serif;font-weight:700;font-size:22px;color:var(--band-head);text-align:center;margin-bottom:18px}
  .feature p{font-weight:300;font-size:12.5px;line-height:18.4px;color:var(--band-text)}
  .feature-divider{position:absolute;top:130px;width:1px;height:150px;background:var(--band-line)}
  .feature-arrow{position:absolute;top:268px}

  /* content */
  .column-title{position:absolute;font-family:"PT Sans",sans-serif;font-weight:700;font-size:21px;color:var(--heading-grey);text-transform:uppercase}
  .thumb{position:absolute;top:878px;width:239px;height:112px;border:2px solid #fff;box-shadow:0 1px 3px rgba(0,0,0,.25)}
  .thumb-investigation{left:127px;background:linear-gradient(100deg,#1d2a55 0%,#344a86 45%,#c8a83a 75%,#7a2c1c 100%)}
  .thumb-forensic{left:431px;background:radial-gradient(circle at 55% 55%,#4fb3d9 0%,#1d5a8a 40%,#0c1f3a 100%)}
  .column-text{position:absolute;top:1006px;width:242px;font-weight:300;font-size:10.5px;line-height:13px;color:var(--muted)}
  .btn-more{position:absolute;top:1112px;width:68px;height:24px;background:#fff;border-radius:3px;box-shadow:0 1px 2px rgba(0,0,0,.2);font-size:9.5px;line-height:24px;text-align:center;color:var(--accent-red)}
  .services-divider{position:absolute;left:738px;top:865px;width:1px;height:275px;background:var(--rule)}
  .service-list{position:absolute;left:764px;top:872px;width:239px;list-style:none}
  .service-list li{display:flex;align-items:center;height:37.7px;border-bottom:1px solid var(--rule);font-family:"PT Sans",sans-serif;font-size:12px;color:#444}
  .service-list li:last-child{border-bottom:none}
  .chev{width:18px;height:18px;background:#f5f5f5;border:1px solid #d0d0d0;border-radius:3px;margin-right:21px;display:flex;align-items:center;justify-content:center}

  /* footer */
  .site-footer{position:absolute;left:0;top:1155px;width:1105px;height:45px;background:var(--footer);text-align:center;color:#fff;font-size:11.5px}
  .footer-links{position:absolute;left:0;width:1105px;top:6px;text-align:center;word-spacing:2px;padding-right:56px}
  .copyright{position:absolute;left:0;width:1105px;top:24px;text-align:center;padding-right:35px}
</style>
</head>
<body>

<header class="site-header">
  <div class="brand"><span class="brand-mark"></span><span class="brand-name">Lantern and Keystone</span></div>
  <div class="utility">LOGIN &nbsp;|&nbsp; SITE MAP</div>
  <div class="header-rule"></div>
  <nav class="main-nav">
    <a class="is-active" href="#">Home</a><a href="#">About</a><a href="#" style="margin-right:34px">Products</a><a href="#" style="margin-right:30px">Services</a><a href="#" style="margin-right:30px">Careers</a><a href="#">Contact</a>
  </nav>
</header>

<section class="hero">
  <div class="hero-photo" role="img" aria-label="Photograph of a masked figure typing on a laptop in blue light"></div>
  <h1 class="hero-title">Lantern and Keystone is a South Australian owned business and we service all of Australia.</h1>
  <div class="btn-gold">Read More</div>
</section>

<section class="band">
  <p class="statement">If you are unsatisfied with the investigation performed by other private investigation agencies and or law enforcement we will continue the investigation until we can provide you with the quality investigation and answers that you seek.</p>
  <div class="band-rule"></div>

  <div class="feature" style="left:104px;width:266px">
    <h3>Digital Forensic</h3>
    <p>Lorem Ipsum is simply dummy text of the printing and typesetting industry. Lorem Ipsum has been the industry's standard dummy text.</p>
  </div>
  <div class="feature-divider" style="left:394px"></div>
  <div class="feature" style="left:412px;width:280px">
    <h3>Missing Persons</h3>
    <p>We will help locate family members, friends and anyone who you care about that have gone missing. Anything from run away to abduction we will use all our resources to help locate these people.</p>
  </div>
  <div class="feature-divider" style="left:706px"></div>
  <div class="feature" style="left:725px;width:292px">
    <h3>Child Recovery</h3>
    <p>Our wide range of resources, skills and experience will help you find your children and get them back to you safe and sound.</p>
  </div>

  <svg class="feature-arrow" style="left:355px" width="18" height="14" viewBox="0 0 18 14"><path d="M1 1l6 6-6 6M9 1l6 6-6 6" fill="none" stroke="var(--gold-deep)" stroke-width="3"/></svg>
  <svg class="feature-arrow" style="left:667px" width="18" height="14" viewBox="0 0 18 14"><path d="M1 1l6 6-6 6M9 1l6 6-6 6" fill="none" stroke="var(--gold-deep)" stroke-width="3"/></svg>
  <svg class="feature-arrow" style="left:982px" width="18" height="14" viewBox="0 0 18 14"><path d="M1 1l6 6-6 6M9 1l6 6-6 6" fill="none" stroke="var(--gold-deep)" stroke-width="3"/></svg>
</section>

<h2 class="column-title" style="left:166px;top:836px">Investigation</h2>
<h2 class="column-title" style="left:470px;top:836px">Digital Forensic</h2>
<h2 class="column-title" style="left:804px;top:836px">Services</h2>

<div class="thumb thumb-investigation" role="img" aria-label="Photograph of a police officer beside a hand holding a radio"></div>
<div class="thumb thumb-forensic" role="img" aria-label="Illustration of a fingerprint scan on a digital network interface"></div>

<p class="column-text" style="left:127px">Lorem Ipsum is simply dummy text of the printing and typesetting industry. Lorem Ipsum has been the industry's standard dummy text ever since the 1500s, when an unknown printer took a galley of type and scrambled it to make a type specimen book. It has survived not only</p>
<p class="column-text" style="left:431px">Lorem Ipsum is simply dummy text of the printing and typesetting industry. Lorem Ipsum has been the industry's standard dummy text ever since the 1500s, when an unknown printer took a galley of type and scrambled it to make a type specimen book. It has survived not only</p>

<div class="btn-more" style="left:125px">READ MORE</div>
<div class="btn-more" style="left:430px">READ MORE</div>

<div class="services-divider"></div>
<ul class="service-list">
  <li><span class="chev"><svg width="6" height="8" viewBox="0 0 6 8"><path d="M1 1l3 3-3 3" fill="none" stroke="#777" stroke-width="1.4"/></svg></span>Unsolved Cases</li>
  <li><span class="chev"><svg width="6" height="8" viewBox="0 0 6 8"><path d="M1 1l3 3-3 3" fill="none" stroke="#777" stroke-width="1.4"/></svg></span>Bullying/Stalking</li>
  <li><span class="chev"><svg width="6" height="8" viewBox="0 0 6 8"><path d="M1 1l3 3-3 3" fill="none" stroke="#777" stroke-width="1.4"/></svg></span>Missing Persons</li>
  <li><span class="chev"><svg width="6" height="8" viewBox="0 0 6 8"><path d="M1 1l3 3-3 3" fill="none" stroke="#777" stroke-width="1.4"/></svg></span>Child recovery</li>
  <li><span class="chev"><svg width="6" height="8" viewBox="0 0 6 8"><path d="M1 1l3 3-3 3" fill="none" stroke="#777" stroke-width="1.4"/></svg></span>Con Men and Con Women</li>
  <li><span class="chev"><svg width="6" height="8" viewBox="0 0 6 8"><path d="M1 1l3 3-3 3" fill="none" stroke="#777" stroke-width="1.4"/></svg></span>Pre-marital checks</li>
  <li><span class="chev"><svg width="6" height="8" viewBox="0 0 6 8"><path d="M1 1l3 3-3 3" fill="none" stroke="#777" stroke-width="1.4"/></svg></span>Corporate and General theft</li>
</ul>

<footer class="site-footer">
  <div class="footer-links">Home &nbsp;| &nbsp;About &nbsp;| &nbsp;Product &nbsp;| &nbsp;Services &nbsp;| &nbsp;Career</div>
  <div class="copyright">©2012 Lantern Keystone, Inc</div>
</footer>

</body>
</html>
```